Gestaltung Mini Katalog für bayerische Polomarke
Gestaltung "Mini" Katalog für bayerische Polomarke
Zielgruppe
Unsere Marke richtet sich an den klassischen Lifestyle Kunden. 20 - 45 Jahre alt, legt Wert auf das Äussere und Kleidung.... Mag es gerne besonders, modern und chic.
Hallo,
wir planen derzeit einen kleinen Katalog von 8-10 Seiten im Format DIN A5 (kein Muss). Präsentiert wird darin die erste bayerische Polomarke K&W reitmode und die aktuellen Kollektionen an Polo-Teamshirts.
Die Fotos dazu werden in den nächsten 14 Tagen entstehen.
Wir suchen nun jemanden, der uns das ganze in eine moderne Gestaltung bringt. Für Vorschläge bitte statt der Fotos alternative Fotos einsetzen.
Unsere Marke bewegt sich im mittleren Preissegment und präsentiert eine ganz besondere Sportart. All das muss in dem Katalog rüber kommen. Neben den Produkt- und Modefotos werden klassische Polobilder integriert, um das Gefühl diesen Sports mit zu vermitteln.
Die Grundfarben sollten sich an denen von K&W reitmode orientieren: schwarz, blau, weiss.... Wobei wir für andere Farben, wenn diese passen bzw. begründet sind auch interessiert sind.

```html
<!DOCTYPE html>
<html lang="de">
<head>
<meta charset="utf-8">
<title>K&amp;W Shirts für Frauen</title>
<link rel="stylesheet" href="https://fonts.googleapis.com/css2?family=EB+Garamond:wght@400;600;700&display=swap">
<style>
  :root {
    --ink: #161616;
    --cyan: #22c3d6;
    --white: #ffffff;
    --paper: #f4f4f4;
    --shirt: #2a2a2a;
  }
  * { margin: 0; padding: 0; box-sizing: border-box; }
  html, body { width: 1198px; height: 1200px; overflow: hidden; background: var(--ink); }
  .page {
    position: relative; width: 1198px; height: 1200px; overflow: hidden;
    background: var(--ink);
    font-family: "EB Garamond", Georgia, serif;
    color: var(--white);
  }
  .title-band {
    position: absolute; left: 0; top: 66px; width: 100%; height: 66px;
    background: var(--cyan);
    border-top: 3px solid var(--white);
    display: flex; align-items: center; padding-left: 24px;
  }
  .title-band h1 { font-weight: 400; font-size: 44px; line-height: 1; color: var(--white); letter-spacing: 0.5px; }
  .product { position: absolute; width: 520px; text-align: center; }
  .product-photo {
    display: block; width: 320px; height: 320px; margin: 0 auto;
    border: 7px solid var(--cyan);
    background: radial-gradient(ellipse at 50% 55%, var(--shirt) 0 42%, var(--paper) 43%);
  }
  .product-name { margin-top: 12px; font-size: 25px; line-height: 1.15; }
  .order-no { font-size: 20px; line-height: 1.2; color: var(--cyan); margin-top: 4px; }
  .sizes { font-size: 20px; line-height: 1.2; margin-top: 3px; }
  .sizes b { font-weight: 700; }
  .price { font-size: 52px; font-weight: 700; color: var(--cyan); line-height: 1; margin-top: 4px; }
  .brand {
    position: absolute; left: 0; top: 598px; width: 1198px; text-align: center;
    font-size: 38px; font-weight: 400; line-height: 1; color: var(--white); letter-spacing: 1px;
  }
  .p1 { left: 41px; top: 162px; }
  .p2 { left: 639px; top: 162px; }
  .p3 { left: 41px; top: 676px; }
  .p4 { left: 639px; top: 676px; }
</style>
</head>
<body>
<main class="page">
  <header class="title-band"><h1>K&amp;W Shirts für Frauen</h1></header>

  <article class="product p1">
    <div class="product-photo" role="img" aria-label="Schwarzes Damen-T-Shirt mit weißem Polo-Motiv"></div>
    <p class="product-name">Shirt für Frauen</p>
    <p class="order-no">Best.-Nr.: 090206</p>
    <p class="sizes">Größen: <b>S - M - L - XL</b></p>
    <p class="price">25,00 €</p>
  </article>

  <article class="product p2">
    <div class="product-photo" role="img" aria-label="Schwarzes Damen-T-Shirt mit blauem Polo-Motiv"></div>
    <p class="product-name">Shirt für Frauen</p>
    <p class="order-no">Best.-Nr.: 090207</p>
    <p class="sizes">Größen: <b>S - M - L - XL</b></p>
    <p class="price">25,00 €</p>
  </article>

  <p class="brand">K&amp;W reitmode</p>

  <article class="product p3">
    <div class="product-photo" role="img" aria-label="Schwarzes Damen-Poloshirt mit Rückennummer 3"></div>
    <p class="product-name">Original Team Shirt 2008 Damen</p>
    <p class="order-no">Best.-Nr.: 080802</p>
    <p class="sizes">Größen: <b>S - M - L - XL</b></p>
    <p class="price">49,00 €</p>
  </article>

  <article class="product p4">
    <div class="product-photo" role="img" aria-label="Schwarzes langärmliges Damen-Poloshirt mit Rückennummer 3"></div>
    <p class="product-name">Original Team Shirt 2008 Damen langärmlig</p>
    <p class="order-no">Best.-Nr.: 080804</p>
    <p class="sizes">Größen: <b>S - M - L - XL</b></p>
    <p class="price">65,00 €</p>
  </article>
</main>
</body>
</html>
```